KDR Business Card

Keystone Draper Resources is a successful and reputable financial services company.Our main services are home loans, commercial loans, vehicle finance and equipment finance. We also do development finance for property developers. Our company is always evolving to always be an industry leader in best financial service practices with access to the largest range of lenders in the country.

We want the business card to reflect our national finance company. Modern, professional corporate image. At the same time the concept of Keystone Draper Resources is that we help build wealth for you but the process for the client is an enjoyable peaceful experience. Not stressful at all .....

Colors to be same as the logo .... gold silver black white as the options

On the reverse side of the card I wanted either just the logo symbol or the logo symbol and text of the logo ....

It could be on a black background ..... or silver or gold .... want it to be quite striking to look at when you first see the card.

On the other side of the card I wanted the following details:

Martin Haldane
Director

0438 927 604

martin@kdrgrp.com.au

Po Box 718
Ferndale ACT 2614

www.kdrgrp.com.au

ACN 618 204 957 (This can be in very small print and can be in the bottom corner of the card or somewhere not very prominent)

As requested Ive uploaded the logo file in both .ai and .pdf formats. Please let me know if you need anything else. Thanks

Reason: Still deciding on which design I like best. I will provide individual feedback as well.

```html
<!DOCTYPE html>
<html lang="en">
<head>
<meta charset="utf-8">
<title>Keystone Draper Resources – Business Card</title>
<link rel="stylesheet" href="https://fonts.googleapis.com/css2?family=Bodoni+Moda:wght@400;500&display=swap">
<style>
  :root {
    --backdrop: #1c110b;
    --card-black: #000000;
    --gold: #d8b85a;
    --gold-edge: #c9a43a;
    --silver-white: #ecebe6;
    --text-light: #e6e6e6;
  }
  html, body {
    margin: 0;
    padding: 0;
    width: 1200px;
    height: 748px;
    overflow: hidden;
    background: var(--backdrop);
  }
  .canvas {
    position: relative;
    width: 1200px;
    height: 748px;
    font-family: "Bodoni Moda", "Times New Roman", serif;
  }
  .card {
    position: absolute;
    width: 492px;
    height: 368px;
    background: var(--card-black);
    border: 1px solid var(--gold-edge);
    border-radius: 16px;
    box-sizing: border-box;
  }
  .card--front { left: 64px; top: 67px; }
  .card--back  { left: 656px; top: 312px; }

  .brand-mark {
    position: absolute;
    border-radius: 50%;
    background: var(--silver-white);
    border: 2px solid #b7bcbc;
    box-sizing: border-box;
  }
  .brand-name {
    position: absolute;
    margin: 0;
    color: var(--gold);
    font-weight: 500;
    text-transform: uppercase;
    letter-spacing: 0.08em;
    line-height: 1.15;
  }

  .card--front .brand-mark { left: 90px; top: 123px; width: 66px; height: 66px; }
  .card--front .brand-name {
    left: 30px; top: 200px; width: 186px;
    text-align: center; font-size: 16px;
  }

  .contact {
    position: absolute;
    right: 33px;
    top: 0;
    text-align: right;
    color: var(--text-light);
    font-weight: 400;
  }
  .contact p { margin: 0; }
  .contact__name  { position: absolute; right: 0; top: 80px;  font-size: 23px; white-space: nowrap; }
  .contact__role  { position: absolute; right: 0; top: 112px; font-size: 14px; }
  .contact__post  { position: absolute; right: 0; top: 177px; font-size: 17px; line-height: 23px; white-space: nowrap; }
  .contact__phone { position: absolute; right: 0; top: 262px; font-size: 17px; white-space: nowrap; }
  .contact__web   { position: absolute; right: 0; top: 312px; font-size: 15.5px; line-height: 19px; white-space: nowrap; }

  .card--back .brand-mark { left: 92px; top: 139px; width: 80px; height: 80px; }
  .card--back .brand-name {
    left: 185px; top: 148px; width: 290px;
    font-size: 24px;
  }
</style>
</head>
<body>
<main class="canvas">
  <section class="card card--front" aria-label="Business card front">
    <span class="brand-mark" aria-hidden="true"></span>
    <p class="brand-name">Keystone Draper Resources</p>
    <div class="contact">
      <p class="contact__name">Martin Haldane</p>
      <p class="contact__role">Director</p>
      <p class="contact__post">Po Box 718<br>Ferndale ACT 2614</p>
      <p class="contact__phone">0438 927 604</p>
      <p class="contact__web">martin@kdrgrp.com.au<br>www.kdrgrp.com.au</p>
    </div>
  </section>

  <section class="card card--back" aria-label="Business card back">
    <span class="brand-mark" aria-hidden="true"></span>
    <p class="brand-name">Keystone Draper Resources</p>
  </section>
</main>
</body>
</html>
```